Creation of a construction/bricklaying business website

Following the template format of "Kestrow 2", the following content would need to be included:
1. Landing page with 3 tiles that go to their own pages.
- Landing page to include background photo and description of services offered.
2. 3 tiles to include:
a) "Contact Us For A Free Quote or Friendly Discussion" Form (middle tile)
b) Case Studies and Testimonials
c) Certifications and Professional Membership
- Design logo to be used from previous ArtQuorum project. Example of logo attached below, please access full JPG files from our account.

Target Market(s)

Prospective clients seeking construction work (bricklaying speciality)

Industry/Entity Type

Residential Construction

Coding

Coded - Design and coding required

Number of Pages Required

4 page

Font styles to use
Sans Serif

Colors

Designer to choose colors to be used in the design.

Requirements
Must have
• Following the template format of "Kestrow 2", the following content would need to be included:
• 1. Landing parent page with 3 tiles that go to the 3 child pages.
• - Landing page to include background photo and description of services offered.
• 2. 3 tiles to include:
• a) "Contact Us For A Free Quote or Friendly Discussion" Form (middle tile)
• b) Case Studies and Testimonials (first tile / left side)
• c) Certifications and Professional Memberships (third tile / right side) (This should include logos of the relevant organisations being displayed. Specifically GLW and the Keel Gate GLW).
• - Design logo to be used from previous ArtQuorum project. Example of logo attached below, please access full JPG files from our account.
Nice to have
• Sleek and modern feel.
• Approachable in terms of how people can contact the company for a quote.
• Traditional pictures to give credibility and comfort around choosing this company.
Should not have
• Cheesy pictures
• Over-complicated
• Simple to use
• Easy URL domain name

```html
<!DOCTYPE html>
<html lang="en">
<head>
<meta charset="utf-8">
<title>R. T. Hallam Construction Ltd</title>
<link rel="stylesheet" href="https://fonts.googleapis.com/css2?family=Libre+Franklin:wght@300;400;500;600;700&display=swap">
<style>
:root{
  --blue:#0f4f9e;
  --blue-dark:#0b3f80;
  --ink:#333a44;
  --muted:#8a8f96;
  --line:#d9dde2;
  --paper:#ffffff;
  --mist:#f4f5f6;
}
*{box-sizing:border-box;margin:0;padding:0}
html,body{width:1200px;height:3571px;overflow:hidden}
body{font-family:"Libre Franklin",Arial,sans-serif;color:var(--ink);background:var(--paper);position:relative}
.abs{position:absolute}
a{color:inherit;text-decoration:none}
.btn{position:absolute;display:flex;align-items:center;justify-content:center;font-size:13px;font-weight:500}
.btn-solid{background:var(--blue);color:#fff}
.btn-white{background:#fff;color:var(--blue)}
.btn-outline{border:1.5px solid #fff;color:#fff}
.btn-outline-blue{border:1.5px solid var(--blue);color:var(--blue)}
.photo{position:absolute}
.section-title{position:absolute;left:0;width:1200px;text-align:center;font-size:30px;font-weight:300;color:#555}
.section-title b{font-weight:600;color:var(--blue)}

/* header */
.site-header{position:absolute;left:0;top:0;width:1200px;height:129px;background:rgba(255,255,255,.93);z-index:2}
.brand{position:absolute;left:88px;top:46px;display:flex;align-items:center;gap:10px;font-size:30px;font-weight:700;color:var(--blue)}
.brand-mark{width:22px;height:22px;background:var(--blue)}
.brand-sub{position:absolute;left:120px;top:86px;font-size:11px;font-weight:700;letter-spacing:1.5px;color:var(--blue)}
.top-phone{position:absolute;left:714px;top:28px;font-size:19px;font-weight:500;display:flex;align-items:center;gap:8px}
.top-phone span{color:var(--blue);font-weight:600}
.main-nav{position:absolute;left:326px;top:81px;display:flex;gap:0;font-size:15px}
.main-nav a{margin-right:37px}
.main-nav .active{color:var(--blue)}

/* hero */
.hero{left:0;top:0;width:1200px;height:626px;background:linear-gradient(110deg,#4a4f55 0%,#6d6f70 35%,#b9b2a8 65%,#d8d3cb 100%)}
.hero-shade{position:absolute;left:0;top:0;width:1200px;height:626px;background:linear-gradient(90deg,rgba(20,25,30,.55),rgba(20,25,30,0) 60%)}
.hero-copy{position:absolute;left:88px;top:272px;font-size:33px;line-height:46px;color:#fff;font-weight:300}
.hero-copy b{font-weight:600}
.hero-arrow{position:absolute;left:1072px;width:36px;height:36px;border-radius:50%;display:flex;align-items:center;justify-content:center}
.dots{position:absolute;display:flex;gap:8px}
.dots i{width:12px;height:12px;border-radius:50%;border:1.5px solid #fff;display:block}
.dots i.on{background:#fff}

/* welcome */
.welcome{left:0;top:626px;width:600px;height:453px;background:var(--mist)}
.welcome-kicker{position:absolute;left:88px;top:728px;font-size:14px;color:#666}
.welcome-title{position:absolute;left:88px;top:750px;font-size:28px;font-weight:400;color:var(--blue)}
.welcome-text{position:absolute;left:88px;top:792px;width:420px;font-size:13px;line-height:21px;color:#aaa}

/* services */
.services{left:0;top:1079px;width:1200px;height:581px;background:var(--blue)}
.tile-title{position:absolute;font-size:16px;font-weight:600;color:#fff}
.tile-text{position:absolute;width:320px;font-size:13px;line-height:22px;color:#e4ebf5}

/* testimonials */
.quote-text{position:absolute;left:250px;top:1830px;width:700px;text-align:center;font-size:15px;line-height:23px;color:#666}
.client-name{position:absolute;left:0;width:1200px;text-align:center}

/* case studies */
.cases{left:0;top:2114px;width:1200px;height:522px;background:var(--mist)}
.case-title{position:absolute;width:300px;font-size:17px;font-weight:600;line-height:23px;color:#333}
.case-date{position:absolute;font-size:13px;color:#555}

/* certifications */
.badge-box{position:absolute;top:2779px;width:160px;height:109px;border:1.5px solid var(--line);background:#fff;display:flex;align-items:center;justify-content:center}
.badge{width:110px;height:58px;border-radius:4px}

/* quote band */
.quote-band{left:0;top:2962px;width:1200px;height:138px;background:var(--blue)}

/* contact */
.contact{left:0;top:3100px;width:1200px;height:471px;background:var(--mist)}
.col-label{position:absolute;top:3273px;font-size:14px;font-weight:600;color:#333}
.col-text{position:absolute;font-size:13px;line-height:21px;color:#555}
.divider{position:absolute;top:3238px;width:1px;height:143px;background:var(--line)}
.social{position:absolute;top:3314px;width:36px;height:36px;border-radius:50%;border:1.5px solid var(--blue)}
.foot-nav{position:absolute;left:208px;top:3430px;display:flex;font-size:14px;color:#666}
.foot-nav a{margin-right:36px}
.foot-nav .active{color:var(--blue)}
.foot-rule{position:absolute;left:88px;top:3488px;width:1024px;height:1px;background:var(--line)}
.copyright{position:absolute;left:0;top:3518px;width:1200px;text-align:center;font-size:12px;color:#666}
</style>
</head>
<body>

<!-- hero -->
<div class="abs hero" role="img" aria-label="Photo of a bright open-plan living room with grey sofa and dining table"></div>
<div class="hero-shade"></div>

<header class="site-header">
  <div class="brand"><span class="brand-mark"></span>R.T.Hallam</div>
  <div class="brand-sub">CONSTRUCTION LTD</div>
  <div class="top-phone">
    <span>Call Us:</span>
    <svg width="22" height="22" viewBox="0 0 24 24"><circle cx="12" cy="12" r="11" fill="none" stroke="#0f4f9e" stroke-width="1.6"/><path d="M8.5 6.5l2 2-1.2 1.5c.8 1.7 2 2.9 3.7 3.7l1.5-1.2 2 2-1.3 1.8c-4-.6-7.3-3.9-7.9-7.9z" fill="#0f4f9e"/></svg>
    07700 900418
  </div>
  <a class="btn btn-solid" style="left:964px;top:19px;width:148px;height:38px">Get a Quote</a>
  <nav class="main-nav">
    <a class="active">-- Home --</a><a>About Us</a><a>Services</a><a>Case Studies</a><a>Testimonials</a><a>Certifications</a><a>Contact Us</a>
  </nav>
</header>

<div class="hero-copy">We believe in <b>full transparency</b><br>and this is reflected in the <b>jobs we<br>quote for you.</b></div>
<a class="btn btn-white" style="left:88px;top:431px;width:148px;height:38px">Explore More</a>
<div class="hero-arrow" style="top:334px;background:rgba(255,255,255,.55)"><svg width="12" height="12" viewBox="0 0 12 12"><path d="M8 1L3 6l5 5" fill="none" stroke="#555" stroke-width="1.8"/></svg></div>
<div class="hero-arrow" style="top:382px;background:#fff"><svg width="12" height="12" viewBox="0 0 12 12"><path d="M4 1l5 5-5 5" fill="none" stroke="#555" stroke-width="1.8"/></svg></div>
<div class="dots" style="left:572px;top:568px"><i></i><i class="on"></i><i></i></div>

<!-- welcome -->
<div class="abs welcome"></div>
<div class="photo" style="left:600px;top:626px;width:600px;height:510px;background:linear-gradient(180deg,#3f77c4 0%,#7fa6d8 45%,#d8d2c6 70%,#b7aea0 100%)" role="img" aria-label="Photo of a newly built two-storey house with timber cladding and scaffolding"></div>
<div class="abs" style="left:585px;top:850px;width:30px;height:3px;background:#5aa0c8"></div>
<div class="welcome-kicker">Welcome to</div>
<div class="welcome-title">R. T. <b style="font-weight:600">Hallam</b> Construction Ltd</div>
<div class="welcome-text">We pride ourselves on attention to detail, pride in our completed project and client satisfaction. We believe in full transparency and this is reflected in the jobs we quote for you. We break down each step with both labour and materials cost so you can see exactly what you are paying for.</div>
<a class="btn btn-solid" style="left:88px;top:938px;width:148px;height:38px">Explore More</a>

<!-- services -->
<div class="abs services"></div>
<div class="photo" style="left:600px;top:1079px;width:600px;height:57px;background:#b7aea0"></div>

<div class="photo" style="left:88px;top:1190px;width:324px;height:186px;background:linear-gradient(160deg,#c9b68e,#8a7a62)" role="img" aria-label="Photo of a house extension under construction with timber frame"></div>
<div class="photo" style="left:438px;top:1190px;width:324px;height:186px;background:linear-gradient(180deg,#8cb6e0,#b08a62 60%,#7a5e44)" role="img" aria-label="Photo of a new build house with roof trusses and scaffolding"></div>
<div class="photo" style="left:788px;top:1190px;width:324px;height:186px;background:linear-gradient(180deg,#9fb6a0,#b7a892 55%,#c7c2b8)" role="img" aria-label="Photo of a stone gabion garden wall beside a paved path"></div>

<div class="tile-title" style="left:88px;top:1400px">Extensions</div>
<div class="tile-title" style="left:438px;top:1400px">New Build / New Houses</div>
<div class="tile-title" style="left:788px;top:1400px">Garden Walls</div>
<div class="tile-text" style="left:88px;top:1432px">Contrary to popular belief, Lorem Ipsum is not simply random text. It has roots in a piece of classical Latin literature from 45 BC, making it over 2000 years old ...</div>
<div class="tile-text" style="left:438px;top:1432px">Contrary to popular belief, Lorem Ipsum is not simply random text. It has roots in a piece of classical Latin literature from 45 BC, making it over 2000 years old ...</div>
<div class="tile-text" style="left:788px;top:1432px">Contrary to popular belief, Lorem Ipsum is not simply random text. It has roots in a piece of classical Latin literature from 45 BC, making it over 2000 years old ...</div>
<a class="btn btn-outline" style="left:88px;top:1548px;width:129px;height:38px">Read More</a>
<a class="btn btn-white" style="left:438px;top:1548px;width:129px;height:38px">Read More</a>
<a class="btn btn-outline" style="left:788px;top:1548px;width:129px;height:38px">Read More</a>

<!-- testimonials -->
<svg class="abs" style="left:584px;top:1734px" width="32" height="24" viewBox="0 0 32 24"><path d="M2 22V13C2 6 6 2 12 1v4c-3 1-5 3-5 7h5v10zM18 22V13c0-7 4-11 10-12v4c-3 1-5 3-5 7h5v10z" fill="#0f4f9e"/></svg>
<div class="section-title" style="top:1768px">What Our <b>Clients Say</b></div>
<div class="quote-text">I asked R.T.Hallam Construction Ltd to build a wall between the public footpath and my property. This job consisted of using old London stock brick and coping stones on top of the wall. The finished product was very good and blended in with the old type of brickwork in the area. I would strongly recommend this company.</div>
<div class="client-name" style="top:1937px;font-size:16px;font-weight:600;color:#333">Helen</div>
<div class="client-name" style="top:1962px;font-size:13px;color:#777">Harwick, Kent</div>
<svg class="abs" style="left:488px;top:1950px" width="10" height="14" viewBox="0 0 10 14"><path d="M8 1L2 7l6 6" fill="none" stroke="#aaa" stroke-width="1.6"/></svg>
<svg class="abs" style="left:698px;top:1950px" width="10" height="14" viewBox="0 0 10 14"><path d="M2 1l6 6-6 6" fill="none" stroke="#0f4f9e" stroke-width="1.8"/></svg>
<a class="btn btn-outline-blue" style="left:536px;top:2005px;width:128px;height:37px">View All</a>

<!-- case studies -->
<div class="abs cases"></div>
<div class="section-title" style="top:2182px">Case <b>Studies</b></div>
<div class="photo" style="left:88px;top:2243px;width:324px;height:183px;background:linear-gradient(180deg,#9cbbe0,#b5876a 50%,#9a8a72)" role="img" aria-label="Photo of a red brick retaining boundary wall"></div>
<div class="photo" style="left:438px;top:2243px;width:324px;height:183px;background:linear-gradient(180deg,#5d7a44,#c9b78e 45%,#4a4a4a)" role="img" aria-label="Photo of a brick parapet wall with stone coping"></div>
<div class="photo" style="left:788px;top:2243px;width:324px;height:183px;background:linear-gradient(180deg,#b9c9d8,#a66a52 45%,#8a8a6a)" role="img" aria-label="Photo of a new red brick garden wall"></div>
<div class="case-title" style="left:88px;top:2450px">Built retaining boundary wall<br>in ealing.</div>
<div class="case-title" style="left:438px;top:2450px;text-decoration:underline">Built parapet wall in<br>chiswick</div>
<div class="case-title" style="left:788px;top:2450px">Built new brick wall in ealing,<br>london</div>
<div class="case-date" style="left:88px;top:2508px">24/05/2018</div>
<div class="case-date" style="left:438px;top:2508px">09/07/2018</div>
<div class="case-date" style="left:788px;top:2508px">01/03/2018</div>
<div class="dots" style="left:576px;top:2549px"><i style="border-color:#0f4f9e"></i><i class="on" style="border-color:#0f4f9e;background:#0f4f9e"></i><i style="border-color:#0f4f9e"></i></div>

<!-- certifications -->
<div class="section-title" style="top:2704px">Certifications &amp; <b>Memberships</b></div>
<svg class="abs" style="left:140px;top:2826px" width="10" height="14" viewBox="0 0 10 14"><path d="M8 1L2 7l6 6" fill="none" stroke="#aaa" stroke-width="1.6"/></svg>
<div class="badge-box" style="left:176px"><div class="badge" style="background:#3a3a3a" role="img" aria-label="Trade association badge"></div></div>
<div class="badge-box" style="left:348px"><div class="badge" style="background:#555" role="img" aria-label="GLW membership badge"></div></div>
<div class="badge-box" style="left:519px"><div class="badge" style="background:#9a9a9a" role="img" aria-label="Building control approval badge"></div></div>
<div class="badge-box" style="left:690px"><div class="badge" style="background:#a11d2c" role="img" aria-label="Trade association badge"></div></div>
<div class="badge-box" style="left:864px"><div class="badge" style="background:#9a9a9a" role="img" aria-label="Building control approval badge"></div></div>
<svg class="abs" style="left:1050px;top:2826px" width="10" height="14" viewBox="0 0 10 14"><path d="M2 1l6 6-6 6" fill="none" stroke="#0f4f9e" stroke-width="1.8"/></svg>

<!-- quote band -->
<div class="abs quote-band"></div>
<div class="abs" style="left:174px;top:3000px;font-size:21px;color:#fff">Get A <b style="font-weight:600">Free Quote</b></div>
<div class="abs" style="left:174px;top:3042px;font-size:14px;color:#e4ebf5">Feel free to get in touch and we can talk through what you are looking to achieve ...</div>
<a class="btn btn-white" style="left:857px;top:3012px;width:167px;height:38px">Get A Quote Now!</a>

<!-- contact -->
<div class="abs contact"></div>
<div class="section-title" style="top:3180px">Contact <b>Us</b></div>
<div class="col-label" style="left:88px">Address:</div>
<div class="col-text" style="left:88px;top:3300px">48 Orchard Row, Harwick,<br>HR4 7QP</div>
<div class="divider" style="left:381px"></div>
<div class="col-label" style="left:437px">Call Us:</div>
<div class="abs" style="left:437px;top:3300px;font-size:22px;color:#555">07700 900418</div>
<div class="col-text" style="left:437px;top:3330px">Email Us: info@rthallam-build.com</div>
<div class="divider" style="left:731px"></div>
<div class="col-label" style="left:788px">Get Social:</div>
<div class="social" style="left:788px" role="img" aria-label="Social profile link"></div>
<div class="social" style="left:836px;background:var(--blue)" role="img" aria-label="Social profile link"></div>
<div class="social" style="left:884px" role="img" aria-label="Social profile link"></div>
<div class="social" style="left:932px" role="img" aria-label="Social profile link"></div>
<svg class="abs" style="left:1076px;top:3316px" width="34" height="34" viewBox="0 0 34 34"><path d="M3 12V31h28V12" fill="none" stroke="#0f4f9e" stroke-width="1.8"/><path d="M17 26V6M10 13l7-7 7 7" fill="none" stroke="#0f4f9e" stroke-width="1.8"/></svg>
<nav class="foot-nav"><a class="active">-- Home --</a><a>About Us</a><a>Services</a><a>Case Studies</a><a>Testimonials</a><a>Certifications</a><a>Contact Us</a></nav>
<div class="foot-rule"></div>
<div class="copyright">© 2018 R. T. Hallam Construction Ltd. All Right Reserved.&nbsp;&nbsp;&nbsp;Privacy Policy | Legal</div>

</body>
</html>
```